Billboard design for a jewelry store.

I am looking for a very unique design with a catchy slogan, I am looking for billboard so good that will make the front page of the newspaper. I want to target customers that are looking for diamond jewelry or diamonds in general. For sure not interested in anything that is genetic or been used in the past. I want the billboard to stand out and very unique. Text not more than 3 words, our logo and an image.

Target Market(s)

Local

Industry/Entity Type

Jewelry Store

Font styles to use
Other font styles liked:
• Open to your suggestion for the font.

Requirements
Must have
• Unique, very brief a catchy slogan. My logo and an image. Open for suggestions. I want also different formats to use on social media.
Nice to have
• I am open to unique and amazing new ideas. I don't want general used design or slogan.
Should not have
• Too much text

```html
<!DOCTYPE html>
<html lang="en">
<head>
<meta charset="utf-8">
<title>Luma Jewelers – Billboard Series</title>
<link rel="stylesheet" href="https://fonts.googleapis.com/css2?family=Yellowtail&family=Dancing+Script:wght@500&display=swap">
<style>
  :root {
    --page: #ffffff;
    --page-edge: #dcdcdc;
    --board: #000000;
    --light: #ffffff;
    --beam-cyan: #00f0ff;
    --beam-red: #ff0000;
    --beam-yellow: #ffff00;
    --beam-magenta: #ff00ff;
    --board-edge: #bdbdbd;
  }
  html, body {
    margin: 0;
    padding: 0;
    overflow: hidden;
    background: var(--page);
  }
  .sheet {
    position: relative;
    width: 1200px;
    height: 922px;
    box-sizing: border-box;
    border: 1px solid var(--page-edge);
    background: var(--page);
    overflow: hidden;
  }
  .billboard {
    position: absolute;
    width: 543px;
    height: 266px;
    display: block;
    outline: 1px solid var(--board-edge);
  }
  .billboard--opulence { left: 33px;  top: 32px; }
  .billboard--wow      { left: 626px; top: 32px; }
  .billboard--trending { left: 33px;  top: 326px; }
  .billboard--she      { left: 626px; top: 326px; }

  .board-ground { fill: var(--board); }
  .light-wedge  { fill: var(--light); }
  .hero-glyph {
    font-family: "Yellowtail", cursive;
    fill: var(--light);
  }
  .tagline {
    font-family: "Dancing Script", cursive;
    font-weight: 500;
    font-size: 8.6px;
    fill: var(--light);
  }
  .wordmark {
    font-family: "Dancing Script", cursive;
    font-weight: 500;
    fill: var(--board);
  }
  .beam--cyan    { fill: var(--beam-cyan); }
  .beam--red     { fill: var(--beam-red); }
  .beam--yellow  { fill: var(--beam-yellow); }
  .beam--magenta { fill: var(--beam-magenta); }
</style>
</head>
<body>
<main class="sheet">

  <svg class="billboard billboard--opulence" viewBox="0 0 516 253" aria-label="Billboard: O – find opulence">
    <rect class="board-ground" width="516" height="253"/>
    <polygon class="light-wedge" points="439,0 469,0 516,98 516,253 327,253"/>
    <polygon class="beam beam--cyan" points="453,0 460,0 421,162"/>
    <text class="hero-glyph" x="52" y="196" font-size="205">O</text>
    <text class="tagline" x="218" y="188">Find opulence in diamonds,</text>
    <text class="tagline" x="218" y="203">jewellery &amp; whole world of luxury</text>
    <text class="wordmark" x="438" y="196" font-size="17" text-anchor="middle">Luma Jewelers</text>
  </svg>

  <svg class="billboard billboard--wow" viewBox="0 0 516 253" aria-label="Billboard: W – find your wow">
    <rect class="board-ground" width="516" height="253"/>
    <polygon class="light-wedge" points="439,0 469,0 516,98 516,253 327,253"/>
    <polygon class="beam beam--red" points="450,0 457,0 418,158"/>
    <text class="hero-glyph" x="40" y="196" font-size="205">w</text>
    <text class="tagline" x="218" y="188">Find your wow in diamonds,</text>
    <text class="tagline" x="218" y="203">jewellery &amp; whole world of luxury</text>
    <text class="wordmark" x="438" y="196" font-size="17" text-anchor="middle">Luma Jewelers</text>
  </svg>

  <svg class="billboard billboard--trending" viewBox="0 0 516 253" aria-label="Billboard: hashtag – discover what's trending">
    <rect class="board-ground" width="516" height="253"/>
    <polygon class="light-wedge" points="439,0 469,0 516,98 516,253 327,253"/>
    <polygon class="beam beam--yellow" points="453,0 460,0 421,162"/>
    <text class="hero-glyph" x="40" y="180" font-size="190">#</text>
    <text class="tagline" x="211" y="175">discover what's trending in</text>
    <text class="tagline" x="211" y="189">diamonds, jewellery &amp; whole world</text>
    <text class="tagline" x="211" y="203">of opulence</text>
    <text class="wordmark" x="448" y="184" font-size="17" text-anchor="middle">Luma Jewelers</text>
  </svg>

  <svg class="billboard billboard--she" viewBox="0 0 516 253" aria-label="Billboard: S – discover she in you">
    <rect class="board-ground" width="516" height="253"/>
    <polygon class="light-wedge" points="439,0 469,0 516,98 516,253 327,253"/>
    <polygon class="beam beam--magenta" points="450,0 457,0 418,160"/>
    <text class="hero-glyph" x="56" y="206" font-size="215">s</text>
    <text class="tagline" x="222" y="175">Discover she in you , find she in</text>
    <text class="tagline" x="222" y="189">diamonds, jewellery &amp; whole world</text>
    <text class="tagline" x="222" y="203">of luxury collection</text>
    <text class="wordmark" x="448" y="184" font-size="17" text-anchor="middle">Luma Jewelers</text>
  </svg>

</main>
</body>
</html>
```